Quorra Pharmacy Brokers Business Card

Hi Desmond - thank you for the Logo - I'm very happy with it.

Can you please design a business card for me using the logo we've decided on.
Updates

Phone Number is (03) 8247 3106 Fax Number is (03) 8247 3107 Please update on the business card Thank you

Industry/Entity Type

Business

```html
<!DOCTYPE html>
<html lang="en">
<head>
<meta charset="utf-8">
<title>Quorra Pharmacy Brokers – Business Card</title>
<link rel="stylesheet" href="https://fonts.googleapis.com/css2?family=Montserrat:wght@500;600;700&display=swap">
<style>
  :root {
    --card: #ffffff;
    --page: #e9e9e9;
    --ink: #1c1c1c;
    --brand-ink: #2a2a2a;
    --icon-grey: #7a7a7a;
  }
  * { margin: 0; padding: 0; box-sizing: border-box; }
  html, body { width: 1200px; height: 816px; overflow: hidden; background: var(--page); }
  .card {
    position: relative;
    width: 1200px; height: 816px;
    background: var(--card);
    border-radius: 56px;
    font-family: "Montserrat", sans-serif;
    color: var(--ink);
  }
  .rule { position: absolute; background: var(--ink); }
  .rule--top { left: 390px; top: 262px; width: 200px; height: 5px; }
  .rule--bottom { left: 80px; top: 386px; width: 510px; height: 6px; }

  .identity { position: absolute; left: 80px; top: 288px; display: flex; align-items: center; gap: 22px; }
  .identity__name { font-size: 26px; font-weight: 700; letter-spacing: 1px; text-transform: uppercase; }
  .identity__title { font-size: 22px; font-weight: 500; letter-spacing: 1.5px; margin-top: 2px; }

  .contacts { position: absolute; left: 80px; top: 440px; display: flex; flex-direction: column; gap: 36px; }
  .contact { display: flex; align-items: center; gap: 28px; }
  .contact__lines { font-size: 22px; font-weight: 500; letter-spacing: 1.5px; line-height: 1.45; }
  .icon { width: 58px; height: 58px; flex: none; }

  .brand {
    position: absolute; right: 90px; top: 372px;
    display: flex; align-items: center; gap: 18px;
    color: var(--brand-ink);
  }
  .brand__mark { width: 22px; height: 22px; background: var(--brand-ink); flex: none; }
  .brand__name { font-size: 32px; font-weight: 600; letter-spacing: 1px; white-space: nowrap; }
</style>
</head>
<body>
<main class="card">
  <div class="rule rule--top"></div>

  <div class="identity">
    <svg class="icon" viewBox="0 0 58 58" aria-hidden="true">
      <circle cx="29" cy="29" r="29" fill="var(--icon-grey)"/>
      <circle cx="29" cy="22" r="9" fill="#fff"/>
      <path d="M13 46c2-9 9-13 16-13s14 4 16 13z" fill="#fff"/>
    </svg>
    <div>
      <p class="identity__name">Desmond Harrow</p>
      <p class="identity__title">Managing Director</p>
    </div>
  </div>

  <div class="rule rule--bottom"></div>

  <div class="contacts">
    <div class="contact">
      <svg class="icon" viewBox="0 0 58 58" aria-hidden="true">
        <circle cx="29" cy="29" r="29" fill="var(--ink)"/>
        <rect x="21" y="14" width="16" height="30" rx="3" fill="#fff"/>
        <rect x="23.5" y="18" width="11" height="20" fill="var(--ink)"/>
        <circle cx="29" cy="41" r="1.5" fill="var(--ink)"/>
      </svg>
      <p class="contact__lines">(03) 8247 3106<br>(03) 8247 3107</p>
    </div>
    <div class="contact">
      <svg class="icon" viewBox="0 0 58 58" aria-hidden="true">
        <circle cx="29" cy="29" r="29" fill="var(--ink)"/>
        <rect x="14" y="17" width="30" height="20" rx="2" fill="none" stroke="#fff" stroke-width="3"/>
        <rect x="25" y="37" width="8" height="5" fill="#fff"/>
        <rect x="20" y="42" width="18" height="3" fill="#fff"/>
      </svg>
      <p class="contact__lines">desmond@quorrabrokers.com<br>quorrabrokers.com</p>
    </div>
    <div class="contact">
      <svg class="icon" viewBox="0 0 58 58" aria-hidden="true">
        <circle cx="29" cy="29" r="29" fill="var(--ink)"/>
        <path d="M29 45s-11-12-11-20a11 11 0 0 1 22 0c0 8-11 20-11 20z" fill="#fff"/>
        <circle cx="29" cy="25" r="4.5" fill="var(--ink)"/>
      </svg>
      <p class="contact__lines">12 Fenwick Lane, Level 4<br>Carrow Street VIC</p>
    </div>
  </div>

  <div class="brand">
    <span class="brand__mark" aria-hidden="true"></span>
    <p class="brand__name">Quorra Pharmacy Brokers</p>
  </div>
</main>
</body>
</html>
```